Brevanta Food Snacks, with three products: snack bars, stand up pouch and cans of superfood products

We need the packaging desing for some heallthy food products we are producing. The product line is based on three: snack bar, stand up poach for muesli and granola and cans for the same. As you know the packaging design with colors and logo and how the ingredients and functionalities in the food industry are one of the most important thing

Target Market(s)

clients from 25 - 45 men and women, looking to have a more healthier diet.

Font styles to use
Sans Serif

Colors
3277b5
ffc214
ffffff
ec1f27
6b449b
fbed22
9ccb3b

Requirements
Must have
• Clear message of the ingredients but simple as possible with the essential information, attractive for the clients
Nice to have
• logo, nice letter and maybe like pictures, innovative pictures of the food product like the silhouette of the nut or chia seed. Colors that could indentify each kinf od productos.
Should not have
• Lot of information, difficult to read everything

```html
<!DOCTYPE html>
<html lang="en">
<head>
<meta charset="utf-8">
<title>Brevanta Food Snacks – Natural Protein Shake Packaging</title>
<link rel="stylesheet" href="https://fonts.googleapis.com/css2?family=Josefin+Sans:wght@700&family=Arimo:ital,wght@0,700;1,400&display=swap">
<style>
  :root {
    --page-bg: #ffffff;
    --pouch-blue: #3f9bea;
    --pouch-green: #a5d93c;
    --title-green: #9ccb3b;
    --can-green: #bdf54a;
    --brand-blue: #3277b5;
    --panel-white: #f4f5f5;
    --band-white: #eceded;
    --ink: #111111;
    --label-grey: #333333;
    --leaf-tone: #dfeec2;
    --food-tone: #eef2f6;
  }
  * { box-sizing: border-box; margin: 0; padding: 0; }
  html, body { width: 1200px; height: 1000px; overflow: hidden; background: var(--page-bg); }
  .canvas { position: relative; width: 1200px; height: 1000px; }

  .sample-label {
    position: absolute; left: 868px; top: 192px;
    font-family: "Arimo", Arial, sans-serif; font-style: italic; font-weight: 400;
    font-size: 33px; color: var(--label-grey);
  }

  .brand-name {
    position: absolute; left: 0; right: 0;
    font-family: "Josefin Sans", sans-serif; font-weight: 700; color: var(--ink);
    text-align: center; font-size: 24px; line-height: 26px;
  }

  .product-title {
    position: absolute; left: 0; right: 0; text-align: center;
    font-family: "Josefin Sans", sans-serif; font-weight: 700;
    font-size: 35px; line-height: 46px; letter-spacing: 1px;
  }

  /* Pouch */
  .pouch {
    position: absolute; left: 180px; top: 270px; width: 373px; height: 480px;
    background: var(--pouch-blue); overflow: hidden;
  }
  .pouch-wave { position: absolute; left: 0; top: 0; width: 373px; height: 480px; }
  .pouch-panel {
    position: absolute; left: 50px; top: 0; width: 271px; height: 366px;
    background: var(--panel-white); border-radius: 0 0 136px 136px;
  }
  .pouch-panel .brand-name { top: 62px; }
  .pouch-panel .product-title { top: 122px; color: var(--title-green); }
  .taste-pill {
    position: absolute; left: 69px; top: 270px; width: 133px; height: 73px;
    border: 3px solid var(--title-green); border-radius: 36px;
    display: flex; align-items: center; justify-content: center; text-align: center;
    font-family: "Josefin Sans", sans-serif; font-weight: 700; font-size: 19px; line-height: 24px;
    color: var(--title-green); padding-top: 4px;
  }
  .leaf-art { position: absolute; width: 36px; height: 150px; background: var(--leaf-tone); opacity: 0.8; border-radius: 18px; }
  .leaf-art--left { left: 8px; top: 172px; }
  .leaf-art--right { left: 328px; top: 172px; }
  .food-art { position: absolute; background: var(--food-tone); opacity: 0.85; border-radius: 40px; }
  .food-art--left { left: 19px; top: 383px; width: 58px; height: 76px; }
  .food-art--right { left: 98px; top: 330px; width: 262px; height: 150px; border-radius: 70px 70px 10px 10px; opacity: 0.5; }
  .pouch-weight {
    position: absolute; left: 170px; top: 440px;
    font-family: "Josefin Sans", sans-serif; font-weight: 700; font-size: 13px; color: var(--ink);
  }

  /* Can */
  .can {
    position: absolute; left: 718px; top: 271px; width: 325px; height: 479px;
    background: var(--can-green); overflow: hidden;
  }
  .can-band { position: absolute; left: 0; right: 0; background: var(--band-white); }
  .can-band--top { top: 0; height: 29px; }
  .can-band--bottom { bottom: 0; height: 19px; }
  .can-panel {
    position: absolute; left: 47px; top: 29px; width: 229px; height: 279px;
    background: var(--panel-white); border-radius: 0 0 115px 115px;
  }
  .can-panel .brand-name { top: 24px; }
  .can-panel .product-title { top: 88px; color: var(--brand-blue); }
  .can-tagline {
    position: absolute; left: 0; right: 0; top: 349px; text-align: center;
    font-family: "Arimo", Arial, sans-serif; font-weight: 700; font-size: 16px; color: var(--brand-blue);
  }
  .taste-button {
    position: absolute; left: 60px; top: 410px; width: 195px; height: 40px;
    background: var(--brand-blue); border-radius: 20px;
    display: flex; align-items: center; justify-content: center; padding-top: 3px;
    font-family: "Josefin Sans", sans-serif; font-weight: 700; font-size: 19px; color: #ffffff; letter-spacing: 0.5px;
  }
  .can-weight {
    position: absolute; left: 272px; top: 434px;
    font-family: "Josefin Sans", sans-serif; font-weight: 700; font-size: 16px; color: var(--brand-blue);
  }
</style>
</head>
<body>
<main class="canvas">
  <p class="sample-label">sample 2</p>

  <section class="pouch" aria-label="Stand up pouch">
    <svg class="pouch-wave" viewBox="0 0 373 480" aria-hidden="true">
      <path d="M0 310 C60 300 110 340 140 380 C170 420 230 400 300 430 C340 446 360 460 373 480 L0 480 Z" fill="var(--pouch-green)"/>
    </svg>
    <div class="leaf-art leaf-art--left" role="img" aria-label="Leafy sprig illustration"></div>
    <div class="leaf-art leaf-art--right" role="img" aria-label="Leafy sprig illustration"></div>
    <div class="food-art food-art--left" role="img" aria-label="Seed pod silhouette"></div>
    <div class="food-art food-art--right" role="img" aria-label="Nut and bean silhouettes"></div>
    <div class="pouch-panel">
      <p class="brand-name">Brevanta<br>Foods</p>
      <h1 class="product-title">NATURAL<br>PROTEIN<br>SHAKE</h1>
      <div class="taste-pill">PRODUCT<br>TASTE</div>
    </div>
    <span class="pouch-weight">50gr</span>
  </section>

  <section class="can" aria-label="Superfood can">
    <div class="can-band can-band--top"></div>
    <div class="can-panel">
      <p class="brand-name">Brevanta<br>Foods</p>
      <h2 class="product-title">NATURAL<br>PROTEIN<br>SHAKE</h2>
    </div>
    <p class="can-tagline">ORGANIC SUPERFOOD MIX</p>
    <div class="taste-button">PRODUCT TASTE</div>
    <span class="can-weight">50gr</span>
    <div class="can-band can-band--bottom"></div>
  </section>
</main>
</body>
</html>
```